Wildlife photographer Website

The website is to be a "resume" of pictures and awards won by Nora. Lean heavy to outdoor wildlife.
She will post articles and have ability to interact with fans.

I will add some of her pictures tonight,

Target Market(s)

Terra Quarterly .....anyone looking to hire a wildlife photographer.

Industry/Entity Type

Professional Photography

Contact Information for Business Card

Nora Falkett
4817 Maple Hollow Lane
Columbia MD 21078
443-581-2094
Nora@FernOwlPix.com

Coding

Coded - Design and coding required

Number of Pages Required

5+ page

Requirements
Must have
• New Logo
Nice to have
• Nature, and eye catching graphics

```html
<!DOCTYPE html>
<html lang="en">
<head>
<meta charset="utf-8">
<title>Nora Falkett — Wildlife Photographer</title>
<link rel="stylesheet" href="https://fonts.googleapis.com/css2?family=Cormorant+Garamond:wght@400;500&family=Poppins:ital,wght@0,300;0,400;0,500;0,600;1,400&display=swap">
<style>
:root{
  --wine:#2b1820;
  --wine-2:#3e2129;
  --plum:#6b3446;
  --plum-soft:#8a5666;
  --ink:#3a2a2f;
  --muted:#7c6f73;
  --paper:#ffffff;
  --line:#b99aa4;
  --cream:#f1e9e4;
}
*{margin:0;padding:0;box-sizing:border-box}
html,body{width:1200px;height:3812px;overflow:hidden;background:var(--paper)}
body{position:relative;font-family:"Poppins",sans-serif;color:var(--ink)}
.abs{position:absolute}
.photo{position:absolute}
.serif{font-family:"Cormorant Garamond",serif}

/* header */
.site-header{position:absolute;left:0;top:0;width:1200px;height:71px;background:var(--paper)}
.brand{left:58px;top:14px;font-size:31px;font-weight:500;color:var(--plum)}
.main-nav{left:407px;top:28px;display:flex;gap:19px;font-size:12.5px;color:var(--ink)}
.main-nav a{color:inherit;text-decoration:none;position:relative}
.main-nav a.active{color:var(--plum)}
.main-nav a.active::after{content:"";position:absolute;left:50%;top:22px;width:5px;height:5px;margin-left:-2.5px;border-radius:50%;background:var(--plum)}
.call{left:981px;top:16px;display:flex;gap:11px;align-items:center}
.call-icon{width:38px;height:38px;border-radius:8px;background:var(--plum);display:flex;align-items:center;justify-content:center}
.call small{display:block;font-size:11px;color:var(--muted)}
.call strong{display:block;font-size:16px;font-weight:600;color:var(--plum);line-height:1.1}

/* hero */
.hero{left:0;top:71px;width:1200px;height:642px;background:var(--wine)}
.hero-tab{left:0;top:712px;width:600px;height:60px;background:var(--wine)}
.hero-title{left:0;top:116px;width:1200px;text-align:center;font-size:47px;color:var(--cream);font-weight:400}
.hero-sub{left:0;top:178px;width:1200px;text-align:center;font-size:16px;color:var(--cream)}
.hero-ring{left:378px;top:170px;width:444px;height:444px;border:1px solid rgba(255,255,255,.12);border-radius:50%}
.big-letter{font-family:"Cormorant Garamond",serif;color:var(--cream);font-size:118px;line-height:1}
.plus-grid{color:rgba(255,255,255,.3);font-size:11px;letter-spacing:6px;line-height:12px}
.chain{color:rgba(255,255,255,.8);font-size:11px;letter-spacing:3px}

/* welcome */
.welcome{left:0;top:845px;width:1200px;text-align:center}
.eyebrow{font-size:14px;color:var(--ink)}
.section-title{font-size:36px;font-weight:500;color:var(--plum);line-height:1.3}
.welcome p.lede{width:490px;margin:20px auto 0;font-size:14.5px;font-style:italic;line-height:21px;color:var(--muted)}
.welcome .role{margin-top:18px;font-size:14px;color:var(--plum);font-weight:500}
.rule{height:1px;background:var(--plum-soft)}

/* about */
.about{left:206px;top:1132px;width:787px;height:416px;background:linear-gradient(100deg,#4a2a33 0%,var(--wine) 70%)}
.about-copy{left:305px;top:70px;width:360px;color:var(--cream)}
.about-copy .eyebrow{color:var(--cream)}
.about-copy h2{font-size:35px;font-weight:400;margin:4px 0 14px}
.about-copy p{font-size:11.5px;line-height:19.5px;margin-bottom:12px;color:#e7dcdf}
.about-copy em{font-size:14px;display:block;margin-top:4px}
.about-contact{left:78px;top:299px;font-size:11.5px;line-height:19px;color:#d9cbd0}
.bio-word{left:882px;top:1390px;font-size:186px;font-weight:200;letter-spacing:14px;color:transparent;-webkit-text-stroke:1px #d7c9cd;line-height:1}

/* gallery */
.gallery-head{left:0;top:1620px;width:1200px;text-align:center}
.explore{left:540px;top:2472px;width:120px;text-align:center;font-size:14px;color:var(--plum);font-weight:500}

/* hire band */
.hire-band{left:0;top:2615px;width:1200px;height:225px;background:linear-gradient(90deg,var(--wine-2),var(--wine))}
.hire-title{left:200px;top:2665px;width:460px;font-size:26px;font-weight:400;font-style:italic;color:var(--cream);line-height:35px}
.hire-contacts{left:200px;top:2749px;display:flex;align-items:center;gap:14px;color:var(--cream)}
.chip{width:33px;height:33px;border-radius:8px;background:#6a3d4a;display:flex;align-items:center;justify-content:center}
.hire-contacts strong{font-size:15px;font-weight:600;margin-right:18px}
.hire-contacts span{font-size:11.5px}

/* articles */
.article-card{position:absolute;width:285px;height:120px;background:var(--paper);padding:28px 22px 0}
.article-card time{display:block;font-size:11px;color:var(--muted)}
.article-card h4{font-size:14px;font-weight:400;line-height:19px;margin-top:10px;color:var(--ink)}
.article-card a{display:block;margin-top:14px;font-size:11.5px;color:var(--plum);text-decoration:none}

/* footer */
.footer{left:0;top:3441px;width:1200px;height:371px;background:var(--wine)}
.footer-tab{left:600px;top:3380px;width:600px;height:62px;background:var(--wine)}
.footer-title{left:0;top:3506px;width:1200px;text-align:center;font-size:38px;font-weight:500;color:var(--cream)}
.social{left:555px;top:3577px;display:flex;gap:17px}
.social i{display:block;width:14px;height:14px;border-radius:50%;border:1.5px solid var(--plum-soft)}
.info-box{left:275px;top:3626px;width:648px;height:59px;border:1px solid #5d3b45;display:flex}
.info-box div{flex:1;display:flex;align-items:center;gap:14px;padding-left:22px;border-right:1px solid #5d3b45}
.info-box div:last-child{border-right:0}
.info-box small{display:block;font-size:11px;color:#b9a6ac}
.info-box b{display:block;font-size:15px;color:var(--cream);font-weight:600}
.info-box p{font-size:11px;color:#b9a6ac}
.footer-links{left:0;top:3724px;width:1200px;text-align:center;font-size:11.5px;color:#cdbcc1}
.copyright{left:0;top:3746px;width:1200px;text-align:center;font-size:11px;color:#a8959b}
</style>
</head>
<body>

<header class="site-header">
  <div class="abs brand">Nora Falkett</div>
  <nav class="abs main-nav">
    <a class="active">Home</a><a>About Me</a><a>Out Door Wildlife</a><a>Articles</a><a>Contact Us</a>
  </nav>
  <div class="abs call">
    <div class="call-icon">
      <svg width="18" height="18" viewBox="0 0 24 24" fill="none" stroke="#fff" stroke-width="2"><path d="M5 3h4l2 5-2.5 1.5a11 11 0 0 0 6 6L16 13l5 2v4a2 2 0 0 1-2 2A17 17 0 0 1 3 5a2 2 0 0 1 2-2z"/></svg>
    </div>
    <div><small>Call Us :</small><strong>443 581 2094</strong></div>
  </div>
</header>

<section>
  <div class="abs hero"></div>
  <div class="abs hero-tab"></div>
  <div class="abs hero-ring"></div>
  <h1 class="abs hero-title serif">I'am Wildlife Photographer</h1>
  <p class="abs hero-sub">Anyone Looking To Hire A Wildlife Photographer</p>

  <div class="photo" role="img" aria-label="Red-headed woodpecker perched on a branch" style="left:249px;top:277px;width:142px;height:167px;background:linear-gradient(160deg,#7da6d6,#6d5a46 65%,#4a3a2c)"></div>
  <div class="photo" role="img" aria-label="Red fox standing in snow" style="left:477px;top:234px;width:247px;height:292px;background:linear-gradient(180deg,#c9c6c2,#b4784a 55%,#d9d6d2)"></div>
  <div class="photo" role="img" aria-label="Loon swimming on blue water" style="left:795px;top:222px;width:169px;height:141px;background:linear-gradient(180deg,#2d5c96,#17376a)"></div>
  <div class="photo" role="img" aria-label="Sandpiper running along the shore" style="left:774px;top:445px;width:216px;height:150px;background:linear-gradient(180deg,#7f8ea0,#c4c1ba)"></div>
  <div class="photo" role="img" aria-label="Flock of birds flying over marsh grass" style="left:244px;top:551px;width:231px;height:127px;background:linear-gradient(180deg,#b6c0c6,#8e7a5a)"></div>

  <div class="abs big-letter" style="left:203px;top:330px">N</div>
  <div class="abs big-letter" style="left:576px;top:468px">O</div>
  <div class="abs big-letter" style="left:880px;top:300px">R</div>

  <div class="abs chain" style="left:400px;top:312px">○○○○○○○○</div>
  <div class="abs chain" style="left:845px;top:368px;width:10px;line-height:11px;font-size:9px">○ ○ ○ ○ ○ ○</div>
  <div class="abs chain" style="left:728px;top:452px">+ + + + +</div>
  <div class="abs chain" style="left:355px;top:458px;width:10px;line-height:11px">+ + + + + + + + +</div>
  <div class="abs plus-grid" style="left:1100px;top:102px;width:50px">+ + + + + + + + + + + + + + + + + + + + + + + + +</div>
  <div class="abs plus-grid" style="left:6px;top:712px;width:50px">+ + + + + + + + + + + + + + + + + + + +</div>
</section>

<section class="abs welcome">
  <div class="eyebrow">Welcome To</div>
  <h2 class="section-title">Nora Falkett</h2>
  <p class="lede">Lorem Ipsum is simply dummy text of the printing and typesetting industry. Lorem Ipsum has been the industry's standard dummy text ever since the 1500s, when an unknown printer Lorem Ipsum is simply dummy text.</p>
  <div class="role">Terra Quarterly Wildlife Photographer</div>
</section>
<div class="abs rule" style="left:450px;top:1076px;width:300px"></div>

<svg class="abs" style="left:166px;top:1090px" width="130" height="176" aria-hidden="true">
  <defs><pattern id="dotgrid" width="11" height="11" patternUnits="userSpaceOnUse"><circle cx="2" cy="2" r="1.6" fill="#d9cfd3"/></pattern></defs>
  <rect width="130" height="176" fill="url(#dotgrid)"/>
</svg>

<section class="abs about">
  <div class="photo" role="img" aria-label="Portrait of Nora outdoors holding a phone among pine trees" style="left:47px;top:50px;width:191px;height:231px;background:linear-gradient(180deg,#4d5a4c,#2b6f84 60%,#a05a4e)"></div>
  <div class="abs about-contact">Phone : 443-581-2094<br>Email : Nora@FernOwlPix.com</div>
  <div class="abs about-copy">
    <div class="eyebrow">About Me</div>
    <h2>Nora Falkett</h2>
    <p>Lorem Ipsum has been the industry's standard dummy text ever since the 1500s, when an unknown printer took a galley of type and scrambled it to make a type.</p>
    <p>It has survived not only five centuries, but also the leap into electronic typesetting, remaining essentially unchanged. It was popularised in the 1960s with the release of Letraset sheets containing Lorem Ipsum passages, and more recently with desktop publishing software like.</p>
    <em>Anyone Looking To Hire A Wildlife Photographer</em>
  </div>
</section>
<div class="abs bio-word">BIO</div>

<section>
  <div class="abs gallery-head">
    <div class="eyebrow">Most Recent Galleries</div>
    <h2 class="section-title">Outdoor Wildlife</h2>
  </div>
  <div class="photo" role="img" aria-label="Woodpecker clinging to a tree trunk" style="left:210px;top:1729px;width:300px;height:398px;background:linear-gradient(100deg,#5c4634 30%,#c9955c 60%,#e3b27c)"></div>
  <div class="photo" role="img" aria-label="Long-tailed duck swimming" style="left:525px;top:1729px;width:225px;height:188px;background:linear-gradient(180deg,#3e5f7c,#1f3a52)"></div>
  <div class="photo" role="img" aria-label="Towhee perched on a wooden rail" style="left:765px;top:1729px;width:225px;height:188px;background:linear-gradient(160deg,#9c8a7a,#5e4a40 60%,#b09888)"></div>
  <div class="photo" role="img" aria-label="Rabbit leaping across snow" style="left:525px;top:1931px;width:465px;height:196px;background:linear-gradient(180deg,#2a3f6a,#7f7162 55%,#c8d0dc)"></div>
  <div class="photo" role="img" aria-label="Red sunset over calm water" style="left:210px;top:2141px;width:780px;height:292px;background:linear-gradient(180deg,#c94a40,#e0724e 45%,#6c4a48 65%,#b2694e)"></div>
  <div class="abs explore">Explore More</div>
  <div class="abs rule" style="left:540px;top:2503px;width:120px"></div>
</section>

<section>
  <div class="abs hire-band"></div>
  <h3 class="abs hire-title">Anyone Looking To Hire A Wildlife Photographer</h3>
  <div class="abs hire-contacts">
    <div class="chip"><svg width="16" height="16" viewBox="0 0 24 24" fill="none" stroke="#fff" stroke-width="1.8"><path d="M5 3h4l2 5-2.5 1.5a11 11 0 0 0 6 6L16 13l5 2v4a2 2 0 0 1-2 2A17 17 0 0 1 3 5a2 2 0 0 1 2-2z"/></svg></div>
    <strong>443-581-2094</strong>
    <div class="chip"><svg width="16" height="16" viewBox="0 0 24 24" fill="none" stroke="#fff" stroke-width="1.8"><rect x="3" y="5" width="18" height="14" rx="2"/><path d="M3 7l9 6 9-6"/></svg></div>
    <span>Nora@FernOwlPix.com</span>
  </div>
  <div class="photo" role="img" aria-label="Red-headed woodpecker on a weathered stump" style="left:740px;top:2534px;width:281px;height:306px;border-radius:40% 40% 0 0;background:linear-gradient(180deg,#b8202e 0%,#f2f0ee 35%,#2a2436 55%,#7a6660 100%)"></div>
</section>

<section>
  <h2 class="abs section-title" style="left:0;top:2905px;width:1200px;text-align:center">Latest Articles</h2>
  <div class="photo" role="img" aria-label="Wave breaking on a frozen shoreline" style="left:206px;top:3001px;width:354px;height:240px;background:linear-gradient(180deg,#2a4f86,#8fb3d6 45%,#27487a)"></div>
  <div class="article-card" style="left:275px;top:3185px">
    <time>25 March 2021</time>
    <h4>Lorem Ipsum has beeN industry's dummy text ever since.</h4>
    <a>Explore More &#9656;</a>
  </div>
  <div class="photo" role="img" aria-label="Cedar waxwings in an evergreen tree" style="left:626px;top:3001px;width:352px;height:240px;background:linear-gradient(140deg,#cfc8bc,#6b7a3c 55%,#3f4a24)"></div>
  <div class="article-card" style="left:688px;top:3185px">
    <time>25 March 2021</time>
    <h4>Lorem Ipsum has beeN industry's dummy text ever since.</h4>
    <a>Explore More &#9656;</a>
  </div>
</section>

<footer>
  <div class="abs footer-tab"></div>
  <div class="abs footer"></div>
  <div class="abs plus-grid" style="left:1158px;top:3380px;width:50px">+ + + + + + + + + + + + + + + + + + + + + + + + + +</div>
  <div class="abs footer-title">Nora Falkett</div>
  <div class="abs social" aria-label="Social profiles"><i></i><i></i><i></i></div>
  <div class="abs info-box">
    <div>
      <svg width="20" height="20" viewBox="0 0 24 24" fill="none" stroke="#8a6a74" stroke-width="1.5"><path d="M12 21s-7-6.5-7-12a7 7 0 0 1 14 0c0 5.5-7 12-7 12z"/><circle cx="12" cy="9" r="2.5"/></svg>
      <span><small>Address</small><p>Out In The Wilderness</p></span>
    </div>
    <div>
      <svg width="20" height="20" viewBox="0 0 24 24" fill="none" stroke="#8a6a74" stroke-width="1.5"><path d="M5 3h4l2 5-2.5 1.5a11 11 0 0 0 6 6L16 13l5 2v4a2 2 0 0 1-2 2A17 17 0 0 1 3 5a2 2 0 0 1 2-2z"/></svg>
      <span><small>Phone</small><b>443-581-2094</b></span>
    </div>
    <div>
      <svg width="20" height="20" viewBox="0 0 24 24" fill="none" stroke="#8a6a74" stroke-width="1.5"><rect x="3" y="5" width="18" height="14" rx="2"/><path d="M3 7l9 6 9-6"/></svg>
      <span><small>Email</small><p>Nora@FernOwlPix.com</p></span>
    </div>
  </div>
  <div class="abs footer-links">Home &nbsp;|&nbsp; About Me &nbsp;|&nbsp; Outdoor Wildlife &nbsp;|&nbsp; Articles &nbsp;|&nbsp; Contact</div>
  <div class="abs copyright">©Nora Falkett - 2021 All Rights reserved.</div>
</footer>

</body>
</html>
```